Marlow Realty Real Estate Brokerage Recruiting Flyer

We are a real estate brokerage looking to hire more real estate agents. We need to list everything we have to offer as a company so real estate agents will join our company. this is our company website: www.Marlowrealty.example .

100% COMMISSION NO MONTHLY FEE
$450 Flat Transaction FEE

What We Offer:
24/7 Office Access
Free E & O Insurance for 1st Year
Free Online CE and PLE
Free 1,000 Business Cards
Free Professional Social Media Marketing
Free Printing, Scanning, and Copies
Free Buyer and Seller Presentation Packages
Free Filquay Cloud Based Document Management Access
Access to our Internal Brokerage Forum
Company Profit Sharing!
Private Offices Available to Rent

*Lead Generation Software with over 3,000 Leads
*10 Leads to Start
* Free Personal CRM and Website
*Restrictions and Rules apply

Company Address:
4817 Amberfield Road
Suite 512
Fairfax, VA 22194
Phone: 703-555-0147
email: info@marlowrealty.example

Target Market(s)

Real Estate Agents

Industry/Entity Type

Real Estate

Colors
0555a3
ffffff

Requirements
Must have
• 100% COMMISSION NO MONTHLY FEE
$450 Flat Transaction FEE

What We Offer:
24/7 Office Access
Free Online CE and PLE
Free 1,000 Business Cards
Company Profit Sharing!

*10 Leads to Start

Company Address:
4817 Amberfield Road
Suite 512
Fairfax, VA 22194
Phone: 703-555-0147

```html
<!DOCTYPE html>
<html lang="en">
<head>
<meta charset="utf-8">
<title>Marlow Realty – Agent Recruiting Flyer</title>
<link href="https://fonts.googleapis.com/css2?family=Raleway:wght@400;500;600;700;800&display=swap" rel="stylesheet">
<style>
  :root{
    --brand-blue:#0555a3;
    --deep-blue:#0a4f9a;
    --sky-blue:#86c8ee;
    --white:#ffffff;
    --ink:#1d2430;
    --muted:#3b4350;
    --stage:#d8d9db;
    --rule:#9aa3ad;
  }
  *{box-sizing:border-box;margin:0;padding:0}
  html,body{width:1200px;height:2229px;overflow:hidden}
  body{background:var(--stage);font-family:"Raleway",sans-serif;color:var(--ink);position:relative}

  .flyer{position:absolute;left:50px;top:407px;width:1100px;height:1415px;background:var(--white);overflow:hidden;box-shadow:0 14px 40px rgba(0,0,0,.25)}
  .hero-art{position:absolute;left:0;top:0;width:1100px;height:790px}

  .logo-plate{position:absolute;left:66px;top:66px;width:357px;height:150px;background:var(--white);border-radius:16px;display:flex;align-items:center;justify-content:center;gap:18px;border:3px solid #cfd8e4}
  .logo-plate .mark{width:34px;height:34px;background:var(--brand-blue)}
  .logo-plate .name{font-weight:700;font-size:40px;color:var(--brand-blue);letter-spacing:1px}

  .site-url{position:absolute;right:40px;top:42px;font-weight:700;font-size:22px;color:var(--ink)}

  .headline{position:absolute;left:276px;top:406px;width:546px;height:143px;background:var(--white);border-radius:10px;display:flex;flex-direction:column;justify-content:center;align-items:center;box-shadow:0 2px 10px rgba(0,0,0,.08)}
  .headline span{display:block;font-weight:800;font-size:44px;line-height:1.15;color:var(--brand-blue)}
  .fee-pill{position:absolute;left:276px;top:563px;width:546px;height:71px;background:var(--brand-blue);border-radius:10px;color:var(--white);font-weight:700;font-size:35px;display:flex;align-items:center;justify-content:center}

  .intro{position:absolute;left:60px;right:60px;top:690px;text-align:center;font-size:24px;line-height:1.45;color:var(--muted);font-weight:500}

  .perks{position:absolute;left:0;top:790px;width:622px;height:484px;background:var(--sky-blue);padding:42px 0 0 66px}
  .perks h2{font-size:26px;font-weight:800;color:var(--ink);margin-bottom:6px}
  .perks ul{list-style:none}
  .perks li{font-size:23px;font-weight:600;line-height:31.5px;color:var(--ink);position:relative;padding-left:26px}
  .perks li::before{content:"";position:absolute;left:2px;top:11px;width:8px;height:8px;border-top:3px solid var(--ink);border-right:3px solid var(--ink);transform:rotate(45deg)}
  .perks li.cont{padding-left:26px}
  .perks li.cont::before{display:none}

  .bonus{position:absolute;left:622px;top:790px;width:478px;height:484px;background:var(--brand-blue)}
  .bonus-grid{position:absolute;left:67px;top:56px;width:342px;height:362px;border:2px solid rgba(255,255,255,.75);display:flex;flex-direction:column}
  .bonus-grid div{flex:1;display:flex;align-items:center;justify-content:center;text-align:center;color:var(--white);font-weight:800;font-size:24px;line-height:1.3;padding:0 20px}
  .bonus-grid div + div{border-top:2px solid rgba(255,255,255,.75)}
  .bonus-grid div.tall{flex:1.35}
  .bonus-grid sup{font-size:13px}
  .fine-print{position:absolute;right:52px;bottom:24px;font-size:13px;font-style:italic;color:rgba(255,255,255,.8)}

  .contact-bar{position:absolute;left:0;top:1274px;width:1100px;height:141px;display:flex;align-items:center;padding-left:66px}
  .contact-bar .col{font-size:23px;line-height:1.4;color:var(--ink);font-weight:500}
  .contact-bar .divider{width:2px;height:62px;background:var(--rule);margin:0 30px}
  .contact-bar strong{font-weight:700}
</style>
</head>
<body>
<main class="flyer">
  <svg class="hero-art" viewBox="0 0 1100 790" aria-hidden="false">
    <defs>
      <linearGradient id="photoTone" x1="0" y1="0" x2="1" y2="1">
        <stop offset="0" stop-color="#b9bcc2"/>
        <stop offset=".45" stop-color="#d9b9a3"/>
        <stop offset=".75" stop-color="#dfe3ea"/>
        <stop offset="1" stop-color="#f4f5f7"/>
      </linearGradient>
      <linearGradient id="fadeDown" x1="0" y1="0" x2="0" y2="1">
        <stop offset=".55" stop-color="#ffffff" stop-opacity="0"/>
        <stop offset="1" stop-color="#ffffff" stop-opacity="1"/>
      </linearGradient>
    </defs>
    <rect width="1100" height="790" fill="#0555a3"/>
    <path d="M517 0 H1100 V790 H0 V652 C80 330 260 80 517 0 Z" fill="#ffffff"/>
    <path role="img" aria-label="Photo of two business people shaking hands" d="M517 0 H1100 V790 H0 V652 C80 330 260 80 517 0 Z" fill="url(#photoTone)"/>
    <path d="M517 0 H1100 V790 H0 V652 C80 330 260 80 517 0 Z" fill="url(#fadeDown)"/>
    <rect x="517" y="0" width="583" height="110" fill="#ffffff"/>
    <path d="M517 0 C260 80 80 330 0 652" fill="none" stroke="#ffffff" stroke-width="6" opacity=".6"/>
  </svg>

  <div class="logo-plate"><span class="mark"></span><span class="name">Marlow Realty</span></div>
  <div class="site-url">www.Marlowrealty.example</div>

  <div class="headline"><span>100% COMMISSION</span><span>NO MONTHLY FEE</span></div>
  <div class="fee-pill">$450 Flat Transaction FEE</div>

  <p class="intro">We are a real estate brokerage looking to hire more real estate agents. We need to list everything we have to offer as a company so real estate agents will join our company.</p>

  <section class="perks">
    <h2>What We Offer:</h2>
    <ul>
      <li>24/7 Office Access</li>
      <li>Free E &amp; O Insurance for 1st Year</li>
      <li>Free Online CE and PLE</li>
      <li>Free 1,000 Business Cards</li>
      <li>Free Professional Social Media Marketing</li>
      <li>Free Printing, Scanning, and Copies</li>
      <li>Free Buyer and Seller Presentation Packages</li>
      <li>Free Filquay Cloud Based Document</li>
      <li class="cont">Management Access</li>
      <li>Access to our Internal Brokerage Forum</li>
      <li>Company Profit Sharing!</li>
      <li>Private Offices Available to Rent</li>
    </ul>
  </section>

  <section class="bonus">
    <div class="bonus-grid">
      <div class="tall">LEAD GENERATION SOFTWARE WITH OVER 3,000 LEADS<sup>*</sup></div>
      <div>10 LEADS TO START<sup>*</sup></div>
      <div class="tall">FREE PERSONAL CRM AND WEBSITE<sup>*</sup></div>
    </div>
    <p class="fine-print">*Restrictions and Rules apply</p>
  </section>

  <footer class="contact-bar">
    <div class="col">4817 Amberfield Road<br>Suite 512, Fairfax, VA 22194</div>
    <span class="divider"></span>
    <div class="col">Phone&nbsp;: <strong>703-555-0147</strong><br>Email&nbsp;&nbsp;: info@marlowrealty.example</div>
    <span class="divider"></span>
    <div class="col">Licensed in<br><strong>D.C., MARYLAND &amp; VIRGINIA</strong></div>
  </footer>
</main>
</body>
</html>
```